Communication Coach needs a business card

https://imgvault-example.net/gallery/1839201/40417/40417_22719043_1839201_8c3e7b2f_preview.png

I like this a lot

I want it to include the following

Delia Strennick
M.A.CCC-SLP
555-204-7718
delia.strennick@mailvento.net
Communication Trainer and Executive Function Coaching
Be Confident-Be Authentic- Be Memorable

on back of card
Public Speaking
Executive Function Coaching
Interview Skills
Corporate Workshops
Self Regulation/Confidence Building

Target Market(s)

adults, parents

Contact Information for Business Card

See above description. i included picture of what i like

Requirements
Must have
• two sides, multi colors ,double sided
Nice to have
• I could have a tag line on front such as Be confident-Be memorable -Be authentic
Should not have
• not too busy or creative as needs to work for corporate setting

```html
<!DOCTYPE html>
<html lang="en">
<head>
<meta charset="utf-8">
<title>Delia Strennick – Business Card</title>
<link rel="stylesheet" href="https://fonts.googleapis.com/css2?family=Roboto+Condensed:wght@400&family=Roboto:wght@400&family=Kaushan+Script&display=swap">
<style>
  :root {
    --bg: #e4e5e7;
    --ink: #2b2b2b;
    --paper: #ffffff;
    --purple: #8b55a0;
    --yellow: #f2d843;
    --pink: #f05e71;
    --teal: #3ab3a7;
    --green: #9acb52;
    --orange: #f47d5a;
  }
  * { box-sizing: border-box; margin: 0; padding: 0; }
  html, body { width: 1200px; height: 1200px; overflow: hidden; }
  body { background: var(--bg); position: relative; font-family: "Roboto", Arial, sans-serif; color: var(--ink); }

  .card {
    position: absolute;
    left: 230px;
    width: 740px;
    height: 488px;
    border-radius: 14px;
    overflow: hidden;
  }

  /* Back side */
  .card-back { top: 62px; }
  .service-stripes { display: flex; height: 410px; }
  .service {
    display: flex;
    align-items: center;
    justify-content: center;
    border-right: 1px solid rgba(255,255,255,0.6);
  }
  .service:last-child { border-right: none; }
  .service span {
    writing-mode: vertical-rl;
    transform: rotate(180deg);
    font-family: "Roboto Condensed", "Arial Narrow", sans-serif;
    font-size: 27px;
    line-height: 1.35;
    text-transform: uppercase;
    text-align: center;
    color: var(--ink);
  }
  .contact-bar {
    height: 78px;
    background: var(--ink);
    color: #fff;
    display: flex;
    align-items: center;
    justify-content: center;
    gap: 22px;
    font-size: 25px;
    letter-spacing: 0.5px;
  }

  .s-purple { background: var(--purple); width: 115px; }
  .s-yellow { background: var(--yellow); width: 128px; }
  .s-pink   { background: var(--pink);   width: 127px; }
  .s-teal   { background: var(--teal);   width: 127px; }
  .s-green  { background: var(--green);  width: 127px; }
  .s-orange { background: var(--orange); width: 116px; }

  /* Front side */
  .card-front { top: 610px; background: var(--paper); }
  .color-band { display: flex; position: absolute; left: 0; right: 0; }
  .color-band div { border-right: 1px solid rgba(255,255,255,0.6); }
  .color-band div:last-child { border-right: none; }
  .band-top { top: 0; height: 44px; }
  .band-bottom { bottom: 0; height: 49px; }

  .tagline {
    position: absolute;
    top: 92px;
    left: 0; right: 0;
    text-align: center;
    font-family: "Roboto Condensed", "Arial Narrow", sans-serif;
    font-size: 26px;
    line-height: 32px;
  }
  .name {
    position: absolute;
    top: 196px;
    left: 0; right: 0;
    text-align: center;
    font-family: "Kaushan Script", cursive;
    font-weight: 400;
    font-size: 84px;
    line-height: 1;
    color: var(--ink);
  }
  .credentials {
    position: absolute;
    top: 322px;
    left: 0; right: 0;
    text-align: center;
    font-family: "Roboto Condensed", "Arial Narrow", sans-serif;
    font-size: 40px;
  }
  .front-contact {
    position: absolute;
    top: 378px;
    left: 0; right: 0;
    display: flex;
    justify-content: center;
    gap: 22px;
    font-size: 27px;
    letter-spacing: 0.4px;
  }
</style>
</head>
<body>

  <section class="card card-back" aria-label="Card back">
    <div class="service-stripes">
      <div class="service s-purple"><span>Public Speaking</span></div>
      <div class="service s-yellow"><span>Executive Function Coaching</span></div>
      <div class="service s-pink"><span>Interview Skills</span></div>
      <div class="service s-teal"><span>Corporate Workshops</span></div>
      <div class="service s-green"><span>Self Regulation/Confidence<br>Building</span></div>
      <div class="service s-orange"></div>
    </div>
    <div class="contact-bar">
      <span>555-204-7718</span><span>|</span><span>delia.strennick@mailvento.net</span>
    </div>
  </section>

  <section class="card card-front" aria-label="Card front">
    <div class="color-band band-top">
      <div class="s-purple"></div><div class="s-yellow"></div><div class="s-pink"></div>
      <div class="s-teal"></div><div class="s-green"></div><div class="s-orange"></div>
    </div>

    <p class="tagline">Communication Trainer and Executive Function Coaching<br>Be Confident-Be Authentic- Be Memorable</p>

    <h1 class="name">Delia Strennick</h1>

    <p class="credentials">M.A.CCC-SLP</p>
    <p class="front-contact"><span>555-204-7718</span><span>|</span><span>delia.strennick@mailvento.net</span></p>

    <div class="color-band band-bottom">
      <div class="s-purple"></div><div class="s-yellow"></div><div class="s-pink"></div>
      <div class="s-teal"></div><div class="s-green"></div><div class="s-orange"></div>
    </div>
  </section>

</body>
</html>
```